National Wood Renewal Company Needs Commercial Brochure

Background:
Q-Vella Timberline Surface Revival is an innovative, affordable cabinet and floor renewal service that renews your wood cabinets and floors without the dust, inconvenience and noxious fumes associated with traditional refinishing methods. In many cases, the process can be completed in just one day! There’s no longer any reason to wait to renew that beautiful wood in your home and now business.
Over time, wooden cabinets and floors can become damaged or faded. Q-Vella can renew their life and luster at a fraction of the cost and without the hassle. In fact, our expert service is usually a fraction of the price of refacing, replacing or refinishing.
Our Q-Vella craftsman can remove the dirt and grime build-up that can make wood look flat and lifeless over time. The renewal process thoroughly cleans the surface, removes old coatings, repairs damaged areas with less mess and applies an elegant finish. You are sure to love the brilliant results. Our Quickglow® process allows our finish to be U.V. cured and our customers love that they can use their floors, cabinets and furniture as soon as soon as we leave their homes.

Objective:
This is a brochure our commercial sales team will use to pitch our wood refinishing services to commercial clients on a regional and national level. With Quickglow® instant cure refinishing we know our product is perfect for commercial clients. We want the commercial clients to have the feeling that our service is not only perfect, but the only solution, for what they need.
Updates

Project Deadline Extended
Reason: I am guaranteeing the rate so I wanted to give more people time.

Target Market(s)

Target Audience:
Our target audience in this case is not an individual, it is an organization. We believe the organization is looking for a need to be fulfilled and not an emotion. We believe in most instances the point of contact will either be the person in charge of maintenance, a general or regional manager, or the corporate office. We are targeting:
• Restaurants
• Retail (department stores, salons, boutiques, etc)
• Hotels / Multi-Family Housing

Industry/Entity Type

Business

Font styles to use
Other font styles liked:
• Our Fonts: (Please use similar for design. Required for final purchased design.) Adobe Garamond-Small Caps & Oldstyle Figures Futura

Requirements
Must have
• InDesign Document Required
25.325 in Width
11 in Height
2 spread trifold for 6 individual pages
Bleed 2 pt

Main Message
The target for this piece does not care as much about pretty photos and catchy taglines as they care about being very clear about what we can do for their business. This needs to be an informative, easy to understand piece.
Do you have scratched, worn-out wood floors, but can’t afford to close your business?
Q-Vella will refinish the hardwood floors in your company during off hours so you can open for business the next day. Our process will be non-disruptive to your business. We can come in after hours, use our U.V. instant-cure refinishing and your floors, furniture and cabinets are ready in the morning.
Nice to have
• Why should they use us?
• Quickglow
• No noxious fumes
• Zero Grit. Zero Fuss. Zero Smell.®
• Lower cost than replacing wood or traditional refinishers
• Non-sandable floor renew – we refinish bamboo, cork and hand scraped flooring

Why wouldn’t they use us?
• Credibility is unknown to them
• Believability is unknown – “Can you really refinish our floors in one day?”
• Cost is unknown
• Is it a necessity right now?
• Apathy to store improvements
Brand Marks
• Q-Vella®
• Quickglow®

The following phrases are also approved for use:
• “Your Wood Floors, Cabinets & Trim Renewed in Hours...Not Days”
• Like-New Wood at a Fraction of the Price (Compared to refacing or replacing)
• Many Jobs Complete in One Day
• Virtually Dust Free
• Dust Free Home
• Odor Free
• Odorless Process
• No Harmful Odors or Fumes
• Clean and Coat
• Renew Life and Luster
• Q-Vella Spares Forests by Keeping What You Have

Website:

http://www.qvellarefresh-example.com/commercial-services/

Photos:
Will supply Quickglow, floor and cabinet photos for design if desired. Feel free to use stock photography placed with watermarks, we will purchase in addition to your payment.

Photos approved:
https://www.filecrate-example.com/sh/7k2mwq84rtpzvb1/hQ4xLm2_Rs

*Additional stock photos also permitted

Our Logos:
https://www.filecrate-example.com/sh/3vbnzq62lpyxkte/5Rw7Kc1_Zd
Our Colors:

Our Fonts: (Please use similar for design. Required for final purchased design.)
Adobe Garamond-Small Caps & Oldstyle Figures
Futura

Should not have

```html
<!DOCTYPE html>
<html lang="en">
<head>
<meta charset="utf-8">
<title>Q-Vella Commercial Brochure Spread</title>
<link rel="stylesheet" href="https://fonts.googleapis.com/css2?family=EB+Garamond:ital,wght@0,400;0,500;0,600;1,400&family=Jost:wght@400;500&display=swap">
<style>
:root{
  --backdrop:#e8e8e6;
  --paper:#fbf8f1;
  --cream:#f2e7cf;
  --gold:#c9962f;
  --gold-deep:#b07e1f;
  --red:#9a1c20;
  --green:#2d7438;
  --ink:#4a3a2c;
  --rule:#8c7c6a;
  --wood-light:#b8683a;
  --wood-mid:#8a3f1f;
  --wood-dark:#4f200f;
  --bar-1:#2c2a2a;
  --bar-2:#ef5a3c;
  --bar-3:#f2c230;
  --bar-4:#5bb147;
  --bar-5:#19a9b5;
  --bar-6:#e3305a;
  --bar-7:#2f62b4;
}
*{box-sizing:border-box;margin:0;padding:0}
html,body{width:1200px;height:800px;overflow:hidden}
body{background:var(--backdrop);font-family:"EB Garamond",Georgia,serif;color:var(--ink)}
.spread{position:absolute;left:60px;top:50px;width:1080px;height:700px;display:flex;box-shadow:0 14px 30px rgba(0,0,0,.18)}
.page{position:relative;width:540px;height:700px;overflow:hidden}
.page--left{background:var(--paper);padding:26px 30px 0 30px}
.page--right{background:linear-gradient(160deg,var(--wood-light) 0%,var(--wood-mid) 45%,var(--wood-dark) 100%)}

.brand{display:flex;flex-direction:column}
.brand__name{display:flex;align-items:center;gap:8px;font-size:44px;font-weight:600;color:var(--red);line-height:1}
.brand__dot{width:14px;height:14px;border-radius:50%;background:var(--green)}
.brand__tag{font-size:17px;color:var(--green);margin-top:4px;letter-spacing:.3px}
.header-rule{height:1px;border-top:1px dashed var(--rule);margin:16px 0 14px}

.columns{display:flex;gap:18px}
.col-data{width:280px}
.col-quotes{width:194px}

.chart{display:block}
.metric-title{font-size:19px;font-weight:500;color:#2b2420;margin-top:8px}
.metric-text{font-size:11.5px;line-height:1.35;margin-top:3px}
.dash-rule{border-top:1px dashed var(--rule);margin:14px 0 10px}
.hardness-table{border-collapse:collapse;margin-top:8px;font-family:"Jost",sans-serif;font-size:8px}
.hardness-table th,.hardness-table td{border:1px solid #9a8c7c;width:26px;height:18px;text-align:center;font-weight:400}
.hardness-table th{height:14px}

.testimonials{background:var(--cream);padding:0 12px 14px;height:496px}
.testimonials__head{background:var(--gold);color:#fff;font-size:18px;font-weight:400;text-align:center;padding:3px 0;margin:0 -12px 10px;clip-path:polygon(0 0,100% 0,94% 100%,0 100%)}
.quote{font-size:11.4px;line-height:1.38;text-align:justify}
.quote__by{text-align:right;font-size:12px;margin-top:8px}
.quote-rule{border-top:1px dashed var(--rule);margin:14px 0}

.footer{position:absolute;left:30px;right:30px;bottom:26px}
.footer__rule{border-top:1.5px solid var(--red);margin-bottom:14px}
.footer__marks{display:flex;justify-content:space-between;align-items:center}
.mark{font-size:22px;font-weight:500}
.mark--brand{color:var(--red)}
.mark--process{color:var(--gold-deep)}

.photo{position:absolute;inset:0}
.badge{position:absolute;left:0;top:0;width:540px;height:160px}
.badge__text{position:absolute;top:28px;left:0;width:540px;text-align:center}
.badge__name{font-size:44px;font-weight:600;color:var(--red);line-height:1;display:inline-flex;align-items:center;gap:8px}
.badge__tag{font-size:17px;color:var(--green);margin-top:4px}
</style>
</head>
<body>
<main class="spread">
  <section class="page page--left">
    <header class="brand">
      <div class="brand__name"><span>Q-Vella</span><span class="brand__dot"></span></div>
      <div class="brand__tag">Timberline Surface Revival™</div>
    </header>
    <div class="header-rule"></div>

    <div class="columns">
      <div class="col-data">
        <svg class="chart" width="280" height="140" viewBox="0 0 280 140" font-family="Jost, sans-serif">
          <line x1="14" y1="6" x2="14" y2="130" stroke="#8c7c6a"/>
          <line x1="14" y1="130" x2="270" y2="130" stroke="#8c7c6a"/>
          <g stroke="#8c7c6a">
            <line x1="10" y1="30" x2="14" y2="30"/><line x1="10" y1="55" x2="14" y2="55"/>
            <line x1="10" y1="80" x2="14" y2="80"/><line x1="10" y1="105" x2="14" y2="105"/>
          </g>
          <g font-size="9" fill="#2b2420" text-anchor="middle">
            <rect x="30" y="56" width="26" height="74" fill="var(--bar-1)"/><text x="43" y="52">9.7</text>
            <rect x="58" y="50" width="26" height="80" fill="var(--bar-2)"/><text x="71" y="46">10</text>
            <rect x="86" y="50" width="26" height="80" fill="var(--bar-3)"/><text x="99" y="46">10</text>
            <rect x="114" y="50" width="26" height="80" fill="var(--bar-4)"/><text x="127" y="46">10</text>
            <rect x="142" y="50" width="26" height="80" fill="var(--bar-5)"/><text x="155" y="46">10</text>
            <rect x="170" y="66" width="26" height="64" fill="var(--bar-6)"/><text x="183" y="62">8</text>
            <rect x="198" y="74" width="26" height="56" fill="var(--bar-7)"/><text x="211" y="70">7</text>
          </g>
          <g font-size="8.5" fill="#fff">
            <text transform="translate(47 126) rotate(-90)">Base Coat</text>
            <text transform="translate(75 126) rotate(-90)">Water Oil</text>
            <text transform="translate(103 126) rotate(-90)" fill="#2b2420">Quickglow</text>
            <text transform="translate(131 126) rotate(-90)">Pro Grade A</text>
            <text transform="translate(159 126) rotate(-90)">Pro Grade B</text>
            <text transform="translate(187 126) rotate(-90)">Oil Poly</text>
            <text transform="translate(215 126) rotate(-90)">Oil Mix</text>
          </g>
        </svg>
        <h3 class="metric-title">Adhesion</h3>
        <p class="metric-text">(Scrape Adhesion): A measure of how well a finish bonds to a surface. A higher number indicates a better bond, with 10 being the maximum capability of test instruments.</p>
        <div class="dash-rule"></div>
        <h3 class="metric-title">Hardness</h3>
        <p class="metric-text">Pencil hardness is rated from 9B (softest) to 9H (hardest).</p>
        <table class="hardness-table">
          <tr><th>1B</th><th>2B</th><th>3B</th><th>4B</th><th>5B</th><th>6B</th><th>7B</th><th>8B</th><th>9B</th></tr>
          <tr><td></td><td></td><td></td><td></td><td></td><td></td><td></td><td></td><td></td></tr>
          <tr><td></td><td></td><td></td><td></td><td></td><td></td><td></td><td></td><td></td></tr>
          <tr><td></td><td></td><td></td><td></td><td></td><td></td><td></td><td></td><td></td></tr>
        </table>
      </div>

      <aside class="col-quotes testimonials">
        <h2 class="testimonials__head">Testimonials</h2>
        <blockquote class="quote">“Our dining room floor was scratched and dull from years of heavy traffic, and we could not afford to close. The crew came in after we locked up, and by morning the floor was finished and cured. We opened for breakfast on time and not one guest smelled a thing.”</blockquote>
        <p class="quote__by">Marla T., Restaurant Manager</p>
        <div class="quote-rule"></div>
        <blockquote class="quote">“We renewed the lobby floors and front desk cabinets at three of our hotels without closing a single room. The work was done overnight with virtually no dust or odor, at a fraction of the cost of replacing the wood. Our guests noticed the difference, never the work.”</blockquote>
        <p class="quote__by">Owen R., Regional Manager</p>
      </aside>
    </div>

    <footer class="footer">
      <div class="footer__rule"></div>
      <div class="footer__marks">
        <span class="mark mark--brand">Q-Vella</span>
        <span class="mark mark--process">Quickglow®</span>
      </div>
    </footer>
  </section>

  <section class="page page--right">
    <div class="photo" role="img" aria-label="Family of three lying on a rich hardwood floor beside a plush toy, seen from above"></div>
    <svg class="badge" viewBox="0 0 540 160" aria-hidden="true">
      <polygon points="40,0 500,0 500,100 270,148 40,100" fill="rgba(255,255,255,.62)"/>
      <polyline points="0,70 270,150 540,70" fill="none" stroke="rgba(255,255,255,.8)" stroke-width="1.2"/>
    </svg>
    <div class="badge__text">
      <div class="badge__name"><span>Q-Vella</span><span class="brand__dot"></span></div>
      <div class="badge__tag">Timberline Surface Revival™</div>
    </div>
  </section>
</main>
</body>
</html>
```